Consulting firm needs an infographic

The consulting we do needs a very graphic and understandable way to have perspective clients get exactly where we can help their company grow. I designed something that needs a lot of spice for it to look professional and relatable to them. This is being created to be used on a business card, as well as on posters, and social media.

```html
<!DOCTYPE html>
<html lang="en">
<head>
<meta charset="utf-8">
<title>Consulting Growth Map</title>
<link rel="stylesheet" href="https://fonts.googleapis.com/css2?family=Montserrat:wght@400;500;700;800&display=swap">
<style>
  :root{
    --bg-center:#f6f2eb;
    --bg-edge:#e5dac8;
    --ink:#585858;
    --heading:#6d5a3c;
    --ring:#e3e1de;
    --yellow:#f8b52d;
    --yellow-light:#f8c85e;
    --yellow-dark:#d48f12;
    --yellow-dot:#f59d00;
    --blue:#3a84dc;
    --blue-light:#6ca6e6;
    --blue-dark:#1b4f8c;
    --blue-dot:#1789c9;
    --green:#9fca3e;
    --green-light:#bad86d;
    --green-dark:#6f8c2a;
    --green-dot:#6f9a1f;
    --pink:#ff1493;
    --pink-light:#f447a6;
    --pink-dark:#8f0f5a;
    --pink-dot:#b8307f;
    --arrow-dark:#7b7b7b;
    --arrow-light:#cfcfcf;
    --hub:#ebe7e1;
    --brand-ink:#4a4a4a;
    --white:#ffffff;
  }
  html,body{margin:0;padding:0;overflow:hidden;}
  body{width:1200px;height:1200px;background:radial-gradient(circle at 50% 50%,var(--bg-center) 0%,var(--bg-edge) 100%);}
  .canvas{display:block;width:1200px;height:1200px;}
  .pill-label{font-family:'Montserrat',sans-serif;font-weight:800;fill:var(--ink);text-anchor:middle;dominant-baseline:central;}
  .company-title{font-family:'Montserrat',sans-serif;font-weight:500;fill:var(--heading);text-anchor:middle;font-size:27px;}
  .company-sub{font-family:'Montserrat',sans-serif;font-weight:400;fill:var(--heading);text-anchor:middle;font-size:20px;}
  .brand-name{font-family:'Montserrat',sans-serif;font-weight:700;fill:var(--brand-ink);text-anchor:middle;dominant-baseline:central;font-size:18px;}
  .font-note{font-family:'Montserrat',sans-serif;font-weight:700;fill:#111;text-anchor:end;font-size:18px;letter-spacing:-0.5px;}
  .ring{fill:var(--ring);}
  .pill{fill:url(#pillFill);}
  .tab-yellow{fill:var(--yellow-dark);opacity:.55;}
  .tab-blue{fill:var(--blue-dark);opacity:.45;}
  .tab-green{fill:var(--green-dark);opacity:.5;}
  .tab-pink{fill:var(--pink-dark);opacity:.45;}
  .dot-yellow{fill:var(--yellow-dot);}
  .dot-blue{fill:url(#blueDot);}
  .dot-green{fill:var(--green-dot);}
  .dot-pink{fill:var(--pink-dot);}
  .icon{fill:var(--white);}
  .icon-line{fill:none;stroke:var(--white);}
  .hub{fill:var(--hub);}
  .arrow{fill:url(#arrowFill);}
</style>
</head>
<body>
<svg class="canvas" viewBox="0 0 1200 1200" xmlns="http://www.w3.org/2000/svg">
  <defs>
    <linearGradient id="pillFill" x1="0" y1="0" x2="0" y2="1">
      <stop offset="0" stop-color="#ffffff"/>
      <stop offset="1" stop-color="#e9e9e9"/>
    </linearGradient>
    <radialGradient id="blueDot" cx="0.4" cy="0.35" r="0.7">
      <stop offset="0" stop-color="#29b1e0"/>
      <stop offset="1" stop-color="#0d6aa8"/>
    </radialGradient>
    <linearGradient id="arrowFill" x1="0" y1="0" x2="1" y2="0">
      <stop offset="0" stop-color="var(--arrow-light)"/>
      <stop offset="1" stop-color="var(--arrow-dark)"/>
    </linearGradient>
    <linearGradient id="yellowFill" x1="0" y1="0" x2="1" y2="1">
      <stop offset="0" stop-color="var(--yellow)"/>
      <stop offset="1" stop-color="var(--yellow-light)"/>
    </linearGradient>
    <linearGradient id="blueFill" x1="0" y1="0" x2="1" y2="1">
      <stop offset="0" stop-color="var(--blue)"/>
      <stop offset="1" stop-color="var(--blue-light)"/>
    </linearGradient>
    <linearGradient id="greenFill" x1="0" y1="0" x2="1" y2="1">
      <stop offset="0" stop-color="var(--green-light)"/>
      <stop offset="1" stop-color="var(--green)"/>
    </linearGradient>
    <linearGradient id="pinkFill" x1="0" y1="0" x2="0" y2="1">
      <stop offset="0" stop-color="var(--pink-light)"/>
      <stop offset="1" stop-color="var(--pink)"/>
    </linearGradient>
    <filter id="softShadow" x="-20%" y="-20%" width="140%" height="140%">
      <feDropShadow dx="3" dy="5" stdDeviation="6" flood-color="#000" flood-opacity=".22"/>
    </filter>
    <filter id="smallShadow" x="-20%" y="-20%" width="140%" height="160%">
      <feDropShadow dx="2" dy="3" stdDeviation="2" flood-color="#000" flood-opacity=".25"/>
    </filter>
    <path id="drop" d="M0 258 L129 129.8 A183 183 0 1 0 -129 129.8 Z"/>
    <path id="arrowShape" d="M-160 -28 L-60 -28 L-60 -62 L0 0 L-60 62 L-60 28 L-160 28 Z"/>
  </defs>

  <!-- connecting arrows -->
  <g class="flow-arrows" filter="url(#smallShadow)">
    <use href="#arrowShape" class="arrow" transform="translate(407,497) rotate(135)"/>
    <use href="#arrowShape" class="arrow" transform="translate(503,783) rotate(45)"/>
    <use href="#arrowShape" class="arrow" transform="translate(776,683) rotate(-45)"/>
    <use href="#arrowShape" class="arrow" transform="translate(689,410) rotate(-135)"/>
  </g>

  <!-- hub -->
  <circle class="hub" cx="601" cy="599" r="93" filter="url(#softShadow)"/>

  <!-- company petal (top) -->
  <g class="petal petal-company" transform="translate(605,239)">
    <circle class="ring" r="196" filter="url(#softShadow)"/>
    <use href="#drop" fill="var(--yellow-dark)"/>
    <use href="#drop" fill="url(#yellowFill)" transform="translate(4,7) scale(.975)"/>
  </g>
  <!-- operations petal (left) -->
  <g class="petal petal-operations" transform="translate(252,590)">
    <circle class="ring" r="196" filter="url(#softShadow)"/>
    <use href="#drop" fill="var(--blue-dark)" transform="rotate(-90)"/>
    <use href="#drop" fill="url(#blueFill)" transform="rotate(-90) translate(-5,6) scale(.975)"/>
  </g>
  <!-- market petal (right) -->
  <g class="petal petal-market" transform="translate(956,605)">
    <circle class="ring" r="194" filter="url(#softShadow)"/>
    <use href="#drop" fill="var(--green-dark)" transform="rotate(90)"/>
    <use href="#drop" fill="url(#greenFill)" transform="rotate(90) translate(4,6) scale(.975)"/>
  </g>
  <!-- structure petal (bottom) -->
  <g class="petal petal-structure" transform="translate(590,954)">
    <circle class="ring" r="196" filter="url(#softShadow)"/>
    <use href="#drop" fill="var(--pink-dark)" transform="rotate(180)"/>
    <use href="#drop" fill="url(#pinkFill)" transform="rotate(180) translate(0,7) scale(.975)"/>
  </g>

  <!-- tip connectors -->
  <g class="connectors">
    <circle cx="602" cy="500" r="12" fill="#f1efec" filter="url(#smallShadow)"/><circle cx="602" cy="500" r="7" class="dot-yellow"/>
    <circle cx="508" cy="589" r="12" fill="#f1efec" filter="url(#smallShadow)"/><circle cx="508" cy="589" r="7" class="dot-blue"/>
    <circle cx="684" cy="602" r="12" fill="#f1efec" filter="url(#smallShadow)"/><circle cx="684" cy="602" r="7" class="dot-green"/>
    <circle cx="592" cy="695" r="12" fill="#f1efec" filter="url(#smallShadow)"/><circle cx="592" cy="695" r="7" class="dot-pink"/>
  </g>

  <!-- firm name in hub -->
  <text class="brand-name" x="601" y="599">Ledgerline</text>

  <!-- company heading -->
  <text class="company-title" x="601" y="149">YOUR COMPANY</text>
  <text class="company-sub" x="601" y="182">PRODUCTS / SERVICES</text>

  <!-- company items -->
  <g class="items items-company" filter="url(#smallShadow)">
    <polygon class="tab-yellow" points="461,228 473,202 733,202 745,228 733,254 473,254"/>
    <rect class="pill" x="475" y="206" width="248" height="44" rx="22"/>
    <circle class="dot-yellow" cx="488" cy="228" r="10"/><circle class="dot-yellow" cx="703" cy="228" r="10"/>
    <polygon class="tab-yellow" points="461,281 473,255 733,255 745,281 733,307 473,307"/>
    <rect class="pill" x="475" y="259" width="248" height="44" rx="22"/>
    <circle class="dot-yellow" cx="488" cy="281" r="10"/><circle class="dot-yellow" cx="703" cy="281" r="10"/>
    <polygon class="tab-yellow" points="461,333 473,307 733,307 745,333 733,359 473,359"/>
    <rect class="pill" x="475" y="311" width="248" height="44" rx="22"/>
    <circle class="dot-yellow" cx="488" cy="333" r="10"/><circle class="dot-yellow" cx="703" cy="333" r="10"/>
  </g>
  <text class="pill-label" x="593" y="229" font-size="24">WORKFORCE</text>
  <text class="pill-label" x="593" y="282" font-size="24">WORKPLACE</text>
  <text class="pill-label" x="593" y="334" font-size="24">WORKFLOW</text>

  <!-- operations items -->
  <g class="items items-operations" filter="url(#smallShadow)">
    <polygon class="tab-blue" points="119,536 131,510 390,510 402,536 390,562 131,562"/>
    <rect class="pill" x="132" y="514" width="250" height="44" rx="22"/>
    <circle class="dot-blue" cx="146" cy="536" r="10"/><circle class="dot-blue" cx="360" cy="536" r="10"/>
    <polygon class="tab-blue" points="119,593 131,567 390,567 402,593 390,619 131,619"/>
    <rect class="pill" x="132" y="571" width="250" height="44" rx="22"/>
    <circle class="dot-blue" cx="146" cy="593" r="10"/><circle class="dot-blue" cx="360" cy="593" r="10"/>
    <polygon class="tab-blue" points="119,652 131,626 390,626 402,652 390,678 131,678"/>
    <rect class="pill" x="132" y="630" width="250" height="44" rx="22"/>
    <circle class="dot-blue" cx="146" cy="652" r="10"/><circle class="dot-blue" cx="360" cy="652" r="10"/>
  </g>
  <text class="pill-label" x="251" y="537" font-size="24">VENDORS</text>
  <text class="pill-label" x="251" y="594" font-size="24">RESOURCES</text>
  <text class="pill-label" x="251" y="653" font-size="24">COSTS</text>

  <!-- market items -->
  <g class="items items-market" filter="url(#smallShadow)">
    <polygon class="tab-green" points="803,555 815,529 1075,529 1087,555 1075,581 815,581"/>
    <rect class="pill" x="815" y="533" width="250" height="44" rx="22"/>
    <circle class="dot-green" cx="830" cy="555" r="10"/><circle class="dot-green" cx="1045" cy="555" r="10"/>
    <polygon class="tab-green" points="803,612 815,586 1075,586 1087,612 1075,638 815,638"/>
    <rect class="pill" x="815" y="590" width="250" height="44" rx="22"/>
    <circle class="dot-green" cx="830" cy="612" r="10"/><circle class="dot-green" cx="1045" cy="612" r="10"/>
    <polygon class="tab-green" points="803,669 815,643 1075,643 1087,669 1075,695 815,695"/>
    <rect class="pill" x="815" y="647" width="250" height="44" rx="22"/>
    <circle class="dot-green" cx="830" cy="669" r="10"/><circle class="dot-green" cx="1045" cy="669" r="10"/>
  </g>
  <text class="pill-label" x="937" y="556" font-size="23">CUSTOMERS</text>
  <text class="pill-label" x="937" y="613" font-size="20">IDENTITY &amp; B&amp;M</text>
  <text class="pill-label" x="937" y="670" font-size="23">REVENUE</text>

  <!-- structure items -->
  <g class="items items-structure" filter="url(#smallShadow)">
    <polygon class="tab-pink" points="473,840 485,814 690,814 702,840 690,866 485,866"/>
    <rect class="pill" x="491" y="818" width="189" height="44" rx="22"/>
    <circle class="dot-pink" cx="507" cy="840" r="10"/><circle class="dot-pink" cx="660" cy="840" r="10"/>
    <polygon class="tab-pink" points="447,918 459,892 718,892 730,918 718,944 459,944"/>
    <rect class="pill" x="460" y="896" width="249" height="44" rx="22"/>
    <circle class="dot-pink" cx="474" cy="918" r="10"/><circle class="dot-pink" cx="689" cy="918" r="10"/>
    <polygon class="tab-pink" points="447,974 459,948 718,948 730,974 718,1000 459,1000"/>
    <rect class="pill" x="460" y="952" width="249" height="44" rx="22"/>
    <circle class="dot-pink" cx="474" cy="974" r="10"/><circle class="dot-pink" cx="689" cy="974" r="10"/>
    <polygon class="tab-pink" points="447,1030 459,1004 718,1004 730,1030 718,1056 459,1056"/>
    <rect class="pill" x="460" y="1008" width="249" height="44" rx="22"/>
    <circle class="dot-pink" cx="474" cy="1030" r="10"/><circle class="dot-pink" cx="689" cy="1030" r="10"/>
  </g>
  <text class="pill-label" x="583" y="842" font-size="21">EXECUTIVE</text>
  <text class="pill-label" x="582" y="920" font-size="20">ADMINISTRATIVE</text>
  <text class="pill-label" x="582" y="975" font-size="23">PERSONNEL</text>
  <text class="pill-label" x="582" y="1031" font-size="23">LOGISTICS</text>

  <!-- reporting arrows -->
  <g class="report-arrows" fill="#f3ecdc">
    <path d="M568 864 L583 880 L574 880 L574 894 L562 894 L562 880 L553 880 Z"/>
    <path d="M605 894 L590 878 L599 878 L599 864 L611 864 L611 878 L620 878 Z"/>
  </g>

  <!-- icons -->
  <g class="icon-home">
    <path class="icon" d="M600 389 L628 418 L620 418 L620 442 L608 442 L608 428 L592 428 L592 442 L580 442 L580 418 L572 418 Z"/>
  </g>
  <g class="icon-gear">
    <circle class="icon-line" cx="447" cy="599" r="22" stroke-width="10" stroke-dasharray="8 6.4"/>
    <circle class="icon-line" cx="447" cy="599" r="15" stroke-width="8"/>
    <circle class="icon-line" cx="447" cy="599" r="6" stroke-width="4"/>
  </g>
  <g class="icon-bulb">
    <circle class="icon" cx="748" cy="595" r="20"/>
    <rect class="icon" x="737" y="612" width="22" height="7" rx="2"/>
    <rect class="icon" x="739" y="622" width="18" height="4" rx="2"/>
    <rect class="icon" x="741" y="629" width="14" height="4" rx="2"/>
    <path d="M737 594 A12 12 0 0 1 748 582" fill="none" stroke="var(--green)" stroke-width="3" stroke-linecap="round" opacity=".6"/>
  </g>
  <g class="icon-clock">
    <circle class="icon-line" cx="591" cy="752" r="25" stroke-width="3.5"/>
    <g class="icon">
      <circle cx="591" cy="735" r="1.8"/><circle cx="591" cy="769" r="1.8"/>
      <circle cx="574" cy="752" r="1.8"/><circle cx="608" cy="752" r="1.8"/>
      <circle cx="599.5" cy="737.3" r="1.5"/><circle cx="605.7" cy="743.5" r="1.5"/>
      <circle cx="605.7" cy="760.5" r="1.5"/><circle cx="599.5" cy="766.7" r="1.5"/>
      <circle cx="582.5" cy="766.7" r="1.5"/><circle cx="576.3" cy="760.5" r="1.5"/>
      <circle cx="576.3" cy="743.5" r="1.5"/><circle cx="582.5" cy="737.3" r="1.5"/>
    </g>
    <path class="icon-line" d="M591 740 L591 753 L584 758" stroke-width="2.5" stroke-linecap="round"/>
  </g>

  <text class="font-note" x="1188" y="1182">Font: Montserrat</text>
</svg>
</body>
</html>
```